Company web site

Looking for a full responsive(mobile friendly) wordpress implementation

Some material is in the website -- brivanta.examplesite.test

But looking for a template more consistent with the logo design, and more future looking.

Target Market(s)

Enterprise Clients

Industry/Entity Type

It Company

Font styles to use
Sans Serif

Colors
33a6d7
0255a3
0455a3
cfdeed
85abd2
3176b5

Requirements
Must have
• about, contact information, partner page, success stories, customer testimonials. links to social presence.
• pricing information

```html
<!DOCTYPE html>
<html lang="en">
<head>
<meta charset="utf-8">
<title>Brivanta – Partners</title>
<link rel="stylesheet" href="https://fonts.googleapis.com/css2?family=Exo+2:wght@400;500;600;700;800&family=Open+Sans:wght@400;600;700&display=swap">
<style>
:root{
  --blue:#29a3dc;
  --blue-dark:#0255a3;
  --topbar:#666769;
  --ink:#555;
  --text:#444;
  --crumb:#e3e3e3;
  --footer:#1d2838;
  --footer-line:#3a4a60;
  --box-line:#cfcfcf;
  --white:#fff;
}
*{margin:0;padding:0;box-sizing:border-box}
html,body{width:1054px;height:1200px;overflow:hidden;background:var(--white)}
body{position:relative;font-family:"Open Sans",sans-serif;color:var(--text)}
.abs{position:absolute}

.topbar{left:0;top:0;width:1054px;height:27px;background:var(--topbar)}
.topbar .call{left:70px;top:6px;font:500 11.5px "Exo 2",sans-serif;color:#eee;display:flex;align-items:center;gap:6px}
.topbar .call b{font-weight:700;color:#fff}
.topbar .social{right:70px;top:0;display:flex;height:27px}
.topbar .social span{width:32px;height:27px;border-left:1px solid #7d7e80;display:flex;align-items:center;justify-content:center}
.topbar .social span:last-child{border-right:1px solid #7d7e80}
.topbar .social i{width:9px;height:9px;border-radius:50%;background:#fff;display:block}

.header{left:0;top:27px;width:1054px;height:85px;background:var(--white)}
.brand{left:70px;top:27px;display:flex;align-items:center;gap:8px;font:700 25px "Exo 2",sans-serif;color:var(--blue)}
.brand i{width:22px;height:22px;border-radius:50%;background:var(--blue);display:block}
.nav{right:70px;top:0;height:85px;display:flex;align-items:center;font:400 15px "Exo 2",sans-serif;color:var(--ink)}
.nav a{color:inherit;text-decoration:none;padding:0 18px}
.nav a.active{background:var(--blue);color:#fff;height:85px;width:100px;display:flex;flex-direction:column;align-items:center;justify-content:center;font-weight:600;padding:0;margin:0 8px;gap:4px}

.hero{left:0;top:112px;width:1054px;height:295px;background:radial-gradient(ellipse at 72% 45%,#1d5d95 0%,#0c2440 35%,#050a12 65%,#000 100%)}
.hero-art{left:540px;top:0;width:514px;height:295px;background:radial-gradient(ellipse at 55% 40%,rgba(120,190,240,.55),rgba(30,80,140,.2) 55%,transparent 75%),linear-gradient(160deg,transparent 60%,rgba(200,140,90,.35) 100%)}
.hero h1{left:70px;top:236px;font:600 29px/36px "Exo 2",sans-serif;color:#e6e6e6}
.hero h1 em{font-style:normal;color:var(--blue)}

.crumb{left:0;top:407px;width:1054px;height:35px;background:var(--crumb);display:flex;align-items:center;padding-left:70px;font:700 12px "Open Sans",sans-serif;color:#555;gap:10px}
.crumb .here{color:var(--blue)}

.section-title{left:0;top:496px;width:1054px;text-align:center;font:800 32px "Exo 2",sans-serif;color:var(--blue);letter-spacing:1px}
.divider{left:282px;top:548px;width:490px;height:14px}
.intro{left:140px;top:586px;width:774px;text-align:center;font:400 14px/20px "Open Sans",sans-serif;color:#555}

.partners{left:70px;top:654px;width:914px;display:grid;grid-template-columns:repeat(5,164px);gap:22px 23.5px}
.partner{height:86px;border:1px solid var(--box-line);border-radius:5px;display:flex;align-items:center;justify-content:center;gap:8px;font:700 22px "Exo 2",sans-serif;color:#333}
.partner i{width:22px;height:22px;border-radius:50%;background:#333;display:block}

.footer{left:0;top:895px;width:1054px;height:265px;background:radial-gradient(circle at 30% 20%,#26344a 0%,var(--footer) 60%)}
.fcol h3{font:500 18px "Exo 2",sans-serif;color:#e8e8e8;padding-bottom:12px;border-bottom:1px solid var(--footer-line);width:118px}
.fcol h3 em{font-style:normal;color:var(--blue)}
.links{list-style:none;margin-top:16px}
.links li{font:400 13.5px "Open Sans",sans-serif;color:#d6d6d6;height:25px;display:flex;align-items:center;gap:8px}
.links li::before{content:"";width:3px;height:3px;border-radius:50%;background:#aaa}
.links li.on{color:var(--blue);font-weight:700}
.links li.on::before{background:var(--blue)}
.contact{margin-top:16px;font:400 13px/17px "Open Sans",sans-serif;color:#d6d6d6}
.contact .name{font-weight:700;color:#fff;font-size:14px}
.contact .row{display:flex;align-items:center;gap:9px;margin-top:12px;font-size:13.5px}
.map{left:516px;top:995px;width:210px;height:135px;border:2px solid #e6e6e6;background:linear-gradient(135deg,#e9e7e3,#d7d5d0)}
.flogo{left:770px;top:1040px;width:220px;text-align:center;font:800 30px "Exo 2",sans-serif;color:var(--blue);letter-spacing:1px}
.fsocial{left:810px;top:1100px;display:flex;gap:26px}
.fsocial i{width:10px;height:10px;border-radius:50%;background:#e6e6e6;display:block}

.copy{left:0;top:1160px;width:1054px;height:40px;background:var(--blue);display:flex;align-items:center;justify-content:center;font:400 13px "Open Sans",sans-serif;color:#eaf6fc}
.copy b{color:#fff;margin:0 3px}
</style>
</head>
<body>

<div class="abs topbar">
  <div class="abs call">
    <svg width="14" height="14" viewBox="0 0 24 24"><path fill="#fff" d="M6.6 10.8a15 15 0 006.6 6.6l2.2-2.2a1 1 0 011-.25 11.4 11.4 0 003.6.57 1 1 0 011 1V20a1 1 0 01-1 1A17 17 0 013 4a1 1 0 011-1h3.5a1 1 0 011 1c0 1.25.2 2.45.57 3.57a1 1 0 01-.25 1z"/></svg>
    Call Us : <b>+123 456 7890</b>
  </div>
  <div class="abs social"><span><i></i></span><span><i></i></span><span><i></i></span><span><i></i></span></div>
</div>

<div class="abs header">
  <div class="abs brand"><i></i>Brivanta</div>
  <nav class="abs nav">
    <a href="#">Home</a>
    <a href="#">Platform</a>
    <a href="#" class="active">
      <svg width="26" height="18" viewBox="0 0 26 18"><circle cx="9" cy="5" r="4" fill="#fff"/><circle cx="17" cy="5" r="4" fill="#fff"/><path d="M1 18c0-5 4-7 8-7s8 2 8 7z" fill="#fff"/><path d="M10 18c0-5 3-7 7-7s8 2 8 7z" fill="#fff"/></svg>
      Partners
    </a>
    <a href="#">Blog</a>
    <a href="#">About</a>
    <a href="#">Contact</a>
  </nav>
</div>

<section class="abs hero">
  <div class="abs hero-art" role="img" aria-label="Hand holding a tablet with a glowing globe and floating network profile panels"></div>
  <h1 class="abs" style="top:124px">Bridging <em>Connected Devices</em><br>With <em>Enterprise Solutions</em></h1>
</section>

<div class="abs crumb">
  <span>HOME</span>
  <svg width="12" height="10" viewBox="0 0 12 10"><path d="M1 1l4 4-4 4M6 1l4 4-4 4" stroke="#29a3dc" stroke-width="1.6" fill="none"/></svg>
  <span class="here">PARTNERS</span>
</div>

<h2 class="abs section-title">PARTNERS</h2>
<svg class="abs divider" viewBox="0 0 490 14"><line x1="0" y1="7" x2="222" y2="7" stroke="#ddd"/><line x1="268" y1="7" x2="490" y2="7" stroke="#ddd"/><circle cx="245" cy="7" r="6" fill="none" stroke="#bbb" stroke-width="2"/></svg>
<p class="abs intro">Lorem ipsum dolor sit amet, consectetur adipiscing elit. Quisque sollicitudin mauris nulla, et interdum felis auctor vitae. Morbi bibendum vulputate nisl at pulvinar.</p>

<div class="abs partners">
  <div class="partner"><i></i>Corvane</div>
  <div class="partner">linkpath</div>
  <div class="partner"><i></i>Halvorsen</div>
  <div class="partner"><i></i>Orbitas</div>
  <div class="partner">Tessaline</div>
  <div class="partner">Quarrydale</div>
  <div class="partner">plainread</div>
  <div class="partner">SureHost</div>
  <div class="partner"><i></i>oak figure</div>
  <div class="partner">vectora</div>
</div>

<footer class="abs footer">
  <div class="abs fcol" style="left:70px;top:42px">
    <h3>Quick <em>Links</em></h3>
    <ul class="links">
      <li class="on">Home</li><li>Platform</li><li>Partners</li><li>Blog</li><li>About</li><li>Contact</li>
    </ul>
  </div>
  <div class="abs fcol" style="left:254px;top:42px">
    <h3 style="width:126px">Contact <em>Details</em></h3>
    <div class="contact">
      <div class="name">Brivanta</div>
      <div>123, Lorem ipsum dolor sit amet,<br>euismod - 123 456</div>
      <div class="row"><svg width="12" height="12" viewBox="0 0 24 24"><path fill="#29a3dc" d="M6.6 10.8a15 15 0 006.6 6.6l2.2-2.2a1 1 0 011-.25 11.4 11.4 0 003.6.57 1 1 0 011 1V20a1 1 0 01-1 1A17 17 0 013 4a1 1 0 011-1h3.5a1 1 0 011 1c0 1.25.2 2.45.57 3.57a1 1 0 01-.25 1z"/></svg>123 456 7890</div>
      <div class="row"><svg width="13" height="12" viewBox="0 0 13 12"><rect x="3" y="0" width="7" height="4" fill="#29a3dc"/><rect x="0" y="4" width="13" height="5" rx="1" fill="#29a3dc"/><rect x="3" y="7" width="7" height="5" fill="#29a3dc" stroke="#1d2838"/></svg>123 456 7890</div>
      <div class="row"><svg width="13" height="10" viewBox="0 0 13 10"><rect width="13" height="10" fill="#29a3dc"/><path d="M0 0l6.5 5L13 0" stroke="#1d2838" fill="none"/></svg>info@brivanta.com</div>
    </div>
  </div>
  <div class="abs fcol" style="left:514px;top:42px">
    <h3 style="width:132px">Location <em>Map</em></h3>
  </div>
  <div class="abs flogo">Brivanta</div>
  <div class="abs fsocial"><i></i><i></i><i></i><i></i></div>
</footer>
<div class="abs map" role="img" aria-label="Street map showing the office location with a red pin"></div>

<div class="abs copy">Copyright © 2017 <b>Brivanta</b>. All Right Reserved.</div>

</body>
</html>
```